Bref créative
Stand out Biz Cards & Stationery for Quarvenix
A Cutting Edge Consulting & Executive Coaching Firm
Simple
Torben K. Aldavisto, PhD
President & CEO
48207 E Corvane Ave
Suite 2875-417
Phoenix, AZ 85093-6718
Torben@Aldavisto-mail.test
www.Aldavisto-mail.test
It might be questionable to use the tag line in the Logo since the font is very tiny.
The significant problems we have, cannot be solved at the same level of thinking with which we created them. -- Gustav Merriwold

```html
<!DOCTYPE html>
<html lang="en">
<head>
<meta charset="utf-8">
<title>Quarvenix Stationery</title>
<link href="https://fonts.googleapis.com/css2?family=Open+Sans:wght@400;600;700&display=swap" rel="stylesheet">
<style>
:root{
  --page:#ffffff;
  --paper:#ffffff;
  --edge:#d6d9de;
  --brand:#1f5fb0;
  --band-dark:#0d4fa8;
  --band-light:#3fa2ea;
  --ink:#3a3f47;
  --muted:#7d8591;
  --faint:#f3d7d3;
}
*{margin:0;padding:0;box-sizing:border-box}
html,body{width:1200px;height:720px;overflow:hidden;background:var(--page);font-family:"Open Sans",Arial,sans-serif;color:var(--ink)}
.canvas{position:relative;width:1200px;height:720px}
.sheet{position:absolute;background:var(--paper);border:1px solid var(--edge);box-shadow:0 2px 6px rgba(0,0,0,.12);overflow:hidden}
.wordmark{font-family:"Open Sans",Arial,sans-serif;font-weight:700;color:var(--brand);letter-spacing:.5px;line-height:1}
.tagline{font-size:5px;color:var(--muted);letter-spacing:.4px;margin-top:2px}
.faint-mark{position:absolute;border-radius:50%;background:var(--faint);opacity:.55}
.band{position:absolute;left:0;right:0;background:linear-gradient(90deg,var(--band-dark),var(--band-light));display:flex;align-items:center;justify-content:space-around;color:#fff;font-size:6px;padding:0 10px}
.band::before{content:"";position:absolute;left:0;right:0;top:-4px;height:1px;background:var(--band-light);opacity:.6}
.band span{display:flex;align-items:center;gap:3px;white-space:nowrap}
.band svg{width:7px;height:7px;fill:#fff}

/* letterhead */
.letterhead{left:43px;top:24px;width:540px;height:672px}
.letterhead .brand{position:absolute;left:30px;top:44px}
.letterhead .wordmark{font-size:30px}
.letterhead .faint-mark{width:150px;height:150px;left:330px;top:410px}
.letterhead .band{bottom:10px;height:18px}

/* business card */
.card-front{left:125px;top:185px;width:206px;height:127px}
.card-front .brand{position:absolute;left:10px;top:12px}
.card-front .wordmark{font-size:21px}
.card-front .person{position:absolute;left:10px;top:47px}
.card-front .name{font-size:9px;color:var(--ink)}
.card-front .role{font-size:5.5px;color:var(--muted);margin-top:1px}
.card-front .contact{position:absolute;left:0;right:0;bottom:0;height:38px;background:linear-gradient(90deg,var(--band-dark),var(--band-light));color:#fff;font-size:4.6px;display:flex;justify-content:space-between;padding:6px 10px;line-height:1.7}
.card-front .contact div span{display:flex;align-items:center;gap:3px}
.card-front .contact svg{width:5px;height:5px;fill:#fff}

.card-back{left:125px;top:336px;width:206px;height:125px;display:flex;align-items:center;justify-content:center;text-align:center;padding:0 22px}
.quote{font-size:5.6px;line-height:1.5;color:var(--ink)}
.quote cite{display:block;font-style:normal;font-weight:600;color:var(--brand)}

/* envelope back */
.envelope-back{left:600px;top:72px;width:576px;height:245px}
.envelope-back .flap{position:absolute;left:0;top:0;width:576px;height:50px}
.envelope-back .seal{position:absolute;left:450px;top:14px;width:14px;height:14px;border-radius:50%;background:#fff}

/* envelope front */
.envelope-front{left:600px;top:360px;width:576px;height:240px}
.envelope-front .brand{position:absolute;left:18px;top:28px}
.envelope-front .wordmark{font-size:26px}
.envelope-front .faint-mark{width:120px;height:120px;left:400px;top:40px}
.envelope-front .band{bottom:12px;height:14px;font-size:5.5px}
</style>
</head>
<body>
<main class="canvas">

  <section class="sheet letterhead" aria-label="Letterhead">
    <div class="brand"><div class="wordmark">Quarvenix</div><div class="tagline">Consulting &amp; Executive Coaching</div></div>
    <div class="faint-mark" aria-hidden="true"></div>
    <footer class="band">
      <span><svg viewBox="0 0 10 10"><path d="M2 1l2 2-1 1.5a6 6 0 0 0 2.5 2.5L7 6l2 2-1.5 1.5C4 9 1 6 .5 2.5z"/></svg>(480) 555-0148</span>
      <span><svg viewBox="0 0 10 10"><path d="M0 2h10v6H0z"/></svg>Torben@Aldavisto-mail.test</span>
      <span>www.Aldavisto-mail.test</span>
      <span><svg viewBox="0 0 10 10"><path d="M5 0a3.5 3.5 0 0 1 3.5 3.5C8.5 6 5 10 5 10S1.5 6 1.5 3.5A3.5 3.5 0 0 1 5 0z"/></svg>48207 E Corvane Ave, Suite 2875-417, Phoenix, AZ 85093-6718</span>
    </footer>
  </section>

  <section class="sheet card-front" aria-label="Business card front">
    <div class="brand"><div class="wordmark">Quarvenix</div></div>
    <div class="person">
      <div class="name">Torben K. Aldavisto, PhD</div>
      <div class="role">President &amp; CEO</div>
    </div>
    <div class="contact">
      <div>
        <span><svg viewBox="0 0 10 10"><path d="M2 1l2 2-1 1.5a6 6 0 0 0 2.5 2.5L7 6l2 2-1.5 1.5C4 9 1 6 .5 2.5z"/></svg>(480) 555-0148</span>
        <span><svg viewBox="0 0 10 10"><path d="M0 2h10v6H0z"/></svg>Torben@Aldavisto-mail.test</span>
        <span>www.Aldavisto-mail.test</span>
      </div>
      <div>
        <span><svg viewBox="0 0 10 10"><path d="M5 0a3.5 3.5 0 0 1 3.5 3.5C8.5 6 5 10 5 10S1.5 6 1.5 3.5A3.5 3.5 0 0 1 5 0z"/></svg>48207 E Corvane Ave</span>
        <span>Suite 2875-417</span>
        <span>Phoenix, AZ 85093-6718</span>
      </div>
    </div>
  </section>

  <section class="sheet card-back" aria-label="Business card back">
    <p class="quote">The significant problems we have, cannot be solved at the same level of thinking with which we created them.<cite>Gustav Merriwold</cite></p>
  </section>

  <section class="sheet envelope-back" aria-label="Envelope back">
    <svg class="flap" viewBox="0 0 576 50" preserveAspectRatio="none" aria-hidden="true">
      <defs><linearGradient id="flapGrad" x1="0" x2="1"><stop offset="0" stop-color="#1a3f9a"/><stop offset="1" stop-color="#3fa2ea"/></linearGradient></defs>
      <polygon points="0,0 576,0 576,18 546,48 30,48 0,18" fill="url(#flapGrad)"/>
    </svg>
    <div class="seal" aria-hidden="true"></div>
  </section>

  <section class="sheet envelope-front" aria-label="Envelope front">
    <div class="brand"><div class="wordmark">Quarvenix</div><div class="tagline">Consulting &amp; Executive Coaching</div></div>
    <div class="faint-mark" aria-hidden="true"></div>
    <footer class="band">
      <span><svg viewBox="0 0 10 10"><path d="M2 1l2 2-1 1.5a6 6 0 0 0 2.5 2.5L7 6l2 2-1.5 1.5C4 9 1 6 .5 2.5z"/></svg>(480) 555-0148</span>
      <span><svg viewBox="0 0 10 10"><path d="M0 2h10v6H0z"/></svg>Torben@Aldavisto-mail.test</span>
      <span>www.Aldavisto-mail.test</span>
      <span><svg viewBox="0 0 10 10"><path d="M5 0a3.5 3.5 0 0 1 3.5 3.5C8.5 6 5 10 5 10S1.5 6 1.5 3.5A3.5 3.5 0 0 1 5 0z"/></svg>48207 E Corvane Ave, Suite 2875-417, Phoenix, AZ 85093-6718</span>
    </footer>
  </section>

</main>
</body>
</html>
```